" Atendimento individual, observando as necessidades do aluno com especial atenção às lacunas de conhecimento (conteúdos que não foram aprendidos/absorvidos adequadamente e que dificultam a compreensão de novos tópicos). Para tanto, preparamos aulas exclusivas para cada aluno, que é sempre visto como um indivíduo independente que devem ter suas necessidades respeitadas. Dessa forma, trabalhamos para estimular conhecimento, criatividade e autonomia, para vencer dificuldades, enfrentar desafios e formar organização pessoal através de um horário fixo de estudos. "

```html
<!DOCTYPE html>
<html lang="pt-BR">
<head>
<meta charset="UTF-8">
<title>Lúcia Amaral – Envelope Saco</title>
<link href="https://fonts.googleapis.com/css2?family=Cormorant+Garamond:wght@400;500&family=Lato:wght@400&display=swap" rel="stylesheet">
<style>
  :root {
    --terracotta: #9c4b32;
    --terracotta-dark: #87402a;
    --terracotta-light: #ad5a3f;
    --paper: #ffffff;
    --backdrop: #d9d9d9;
    --text-light: #f3e4dc;
  }
  * { margin: 0; padding: 0; box-sizing: border-box; }
  html, body {
    width: 1200px;
    height: 1200px;
    overflow: hidden;
    background: var(--backdrop);
  }
  .sheet {
    width: 1200px;
    height: 1200px;
    display: flex;
    align-items: center;
    justify-content: center;
    gap: 80px;
  }
  .envelope {
    position: relative;
    width: 460px;
    height: 640px;
    box-shadow: 0 6px 18px rgba(0,0,0,0.18);
  }

  /* Back of envelope */
  .envelope--back {
    background: var(--terracotta);
    color: var(--text-light);
    overflow: hidden;
  }
  .envelope--back .decoration {
    position: absolute;
    left: 40px;
    top: 60px;
    width: 300px;
    height: 300px;
  }
  .envelope--back .contact {
    position: absolute;
    left: 0;
    right: 0;
    bottom: 70px;
    text-align: center;
    font-family: 'Lato', sans-serif;
    font-size: 11px;
    line-height: 1.8;
    letter-spacing: 0.3px;
  }
  .envelope--back .contact .brand-small {
    font-family: 'Cormorant Garamond', serif;
    font-size: 20px;
    letter-spacing: 1px;
    margin-bottom: 14px;
  }

  /* Front of envelope */
  .envelope--front {
    background: var(--paper);
  }
  .envelope--front .flap {
    position: absolute;
    top: 0;
    left: 0;
    right: 0;
    height: 52px;
    background: var(--terracotta);
  }
  .envelope--front .logo {
    position: absolute;
    top: 230px;
    left: 0;
    right: 0;
    text-align: center;
    color: var(--terracotta);
    font-family: 'Cormorant Garamond', serif;
  }
  .logo .brand-name {
    font-size: 42px;
    font-weight: 500;
    letter-spacing: 1px;
    text-transform: uppercase;
  }
  .logo .tagline {
    margin-top: 2px;
    font-size: 13px;
    letter-spacing: 4px;
    text-transform: uppercase;
  }
  .envelope--front .footer {
    position: absolute;
    left: 36px;
    right: 36px;
    bottom: 40px;
  }
  .footer .web {
    font-family: 'Lato', sans-serif;
    font-size: 11px;
    color: var(--terracotta);
    letter-spacing: 0.5px;
    margin-bottom: 8px;
  }
  .footer .rule {
    height: 3px;
    background: var(--terracotta);
  }
  .footer .rule + .rule {
    margin-top: 4px;
    height: 1px;
  }
</style>
</head>
<body>
  <main class="sheet">
    <section class="envelope envelope--back" aria-label="Verso do envelope">
      <svg class="decoration" role="img" aria-label="Ornamento decorativo em tom sobre tom" viewBox="0 0 300 300">
        <defs>
          <radialGradient id="ornamentTone" cx="50%" cy="50%" r="50%">
            <stop offset="0%" stop-color="#ad5a3f" stop-opacity="0.55"/>
            <stop offset="100%" stop-color="#9c4b32" stop-opacity="0"/>
          </radialGradient>
        </defs>
        <rect width="300" height="300" fill="url(#ornamentTone)"/>
      </svg>
      <div class="contact">
        <div class="brand-small">Lúcia Amaral</div>
        <div>+55 (11) 4000-1234 &nbsp;|&nbsp; +55 (11) 4000-5678</div>
        <div>contato@luciaamaral.com.br</div>
        <div>Rua das Acácias, 120 | Centro | Campinas | SP | Brasil</div>
      </div>
    </section>

    <section class="envelope envelope--front" aria-label="Frente do envelope">
      <div class="flap"></div>
      <div class="logo">
        <div class="brand-name">Lúcia Amaral</div>
        <div class="tagline">Espaço Educacional</div>
      </div>
      <div class="footer">
        <div class="web">www.luciaamaral.com.br</div>
        <div class="rule"></div>
        <div class="rule"></div>
      </div>
    </section>
  </main>
</body>
</html>
```